Pel'k Marrowind Travel

We need a sleek, professional, inviting card to elicit global travel for the experienced and professional traveler. Royal blue, black and silver. (perhaps the wording could be silver with black shadow?-get creative) Maybe a watermark on the front and the full raised logo on the back.
We want a stylish and modern card, but professional.

```html
<!DOCTYPE html>
<html lang="en">
<head>
<meta charset="utf-8">
<title>Pel'k Marrowind Travel — Business Card</title>
<link href="https://fonts.googleapis.com/css2?family=Josefin+Sans:wght@600;700&display=swap" rel="stylesheet">
<style>
  :root {
    --royal: #00138f;
    --sky: #4fd3f7;
    --lime: #7ef22a;
    --ink: #111111;
    --paper: #ffffff;
    --backdrop: #ffffff;
  }
  * { box-sizing: border-box; margin: 0; padding: 0; }
  html, body {
    width: 1200px;
    height: 1000px;
    overflow: hidden;
    background: var(--backdrop);
    font-family: "Josefin Sans", sans-serif;
  }
  .canvas {
    position: relative;
    width: 1200px;
    height: 1000px;
  }
  .card {
    position: absolute;
    left: 240px;
    width: 720px;
    height: 411px;
    box-shadow: 4px 5px 10px rgba(0, 0, 0, 0.22);
  }
  .card--front {
    top: 71px;
    background: var(--royal);
    display: flex;
    align-items: center;
    justify-content: center;
  }
  .card--back {
    top: 530px;
    background: var(--paper);
  }
  .brand {
    display: flex;
    align-items: center;
    gap: 14px;
  }
  .brand__dot {
    width: 18px;
    height: 18px;
    border-radius: 50%;
    background: var(--lime);
    flex: none;
  }
  .brand__name {
    color: var(--sky);
    font-weight: 700;
    text-transform: uppercase;
    line-height: 1.05;
    text-align: center;
  }
  .card--front .brand__name { font-size: 34px; }
  .card--back .brand {
    position: absolute;
    left: 0;
    width: 359px;
    top: 205px;
    transform: translateY(-50%);
    justify-content: center;
  }
  .card--back .brand__name { font-size: 24px; }
  .card--back .brand__dot { width: 13px; height: 13px; }
  .divider {
    position: absolute;
    left: 357px;
    top: 77px;
    width: 3px;
    height: 256px;
    background: var(--sky);
  }
  .contact {
    position: absolute;
    left: 411px;
    top: 100px;
    color: var(--ink);
    font-weight: 600;
  }
  .contact__name {
    font-size: 26px;
    font-weight: 700;
    line-height: 1;
    color: var(--sky);
  }
  .contact__name span { color: var(--lime); }
  .contact__role {
    font-size: 16px;
    margin-top: 4px;
  }
  .contact__address {
    margin-top: 46px;
    font-size: 16px;
    line-height: 21px;
  }
  .contact__lines {
    margin-top: 20px;
    list-style: none;
    font-size: 16px;
    line-height: 21px;
  }
  .contact__lines li { display: flex; }
  .contact__label {
    width: 24px;
    color: var(--sky);
  }
</style>
</head>
<body>
<main class="canvas">
  <section class="card card--front" aria-label="Card front">
    <div class="brand">
      <span class="brand__dot"></span>
      <p class="brand__name">Pel'k Marrowind<br>Travel</p>
    </div>
  </section>

  <section class="card card--back" aria-label="Card back">
    <div class="brand">
      <span class="brand__dot"></span>
      <p class="brand__name">Pel'k Marrowind<br>Travel</p>
    </div>
    <div class="divider"></div>
    <div class="contact">
      <h1 class="contact__name">SAMPLE <span>NAME</span></h1>
      <p class="contact__role">Sample Position</p>
      <p class="contact__address">Sample Address, Unit #<br>City, 12345</p>
      <ul class="contact__lines">
        <li><span class="contact__label">P</span>123-456-7890</li>
        <li><span class="contact__label">E</span>sampleemail@pelkmail.com</li>
        <li><span class="contact__label">W</span>www.samplewebsite.com</li>
      </ul>
    </div>
  </section>
</main>
</body>
</html>
```